TalvenInsight card back

Our company already has a logo and we have business cards. (I have included a picture of my business card front that i plan to use.) I want to promote a new division of Talven, called "TalvenInsight" and would like the back side of my card designed to promote this division using the same color scheme and concept as front. So I'm looking for a design for the TalvenInsight (back) side of my card. This back side does need any contact info - including that it doesn't need my name, phone, email etc. I have included the tag line that I would like to have included on that TalvenInsight side of the card. But i'd like the design to reflect "wisdom" but using a similar theme as in our sun logo. One concept i have for this side of the card has the sun is entirely out of the box and lighting up a spacious blue background to the card. Then there's a "TalvenInsight" as well as the tag line. I welcome concepts along these lines or others that you may have. Thanks!

Target Market(s)

High-end energy, or technology firms. Business leaders within the firm.

Industry/Entity Type

Professional Service

Contact Information for Business Card

The card will be double sided, but i only the need the single TalvenInsight side designed. It has to coordinate with the front side (I've included a picture of it) in color, etc.

Logo Text

TalvenInsight

Font styles to use
Other font styles liked:
• font from existing card front

Requirements
Must have
• The tie in with the Talven sun from our logo. A sense of spaciousness and/or clarity that comes from enlightened wisdom. A professional feel but a feel good feel too. The division label "TalvenInsight" and in a similar font as the existing business card. The tag line.
Should not have
• The back, TalvenINsight, side should not have contact info and should not repeat any of the front side info, given that it will be printed on the back side of card.

```html
<!DOCTYPE html>
<html lang="en">
<head>
<meta charset="utf-8">
<title>TalvenInsight Business Card</title>
<link href="https://fonts.googleapis.com/css2?family=Source+Sans+3:ital,wght@0,400;0,600;0,700;1,400&display=swap" rel="stylesheet">
<style>
  :root {
    --navy: #0b3768;
    --orange: #f5841f;
    --warm-light: #fcc23a;
    --paper: #ffffff;
    --stage: #e4e5e7;
  }
  * { margin: 0; padding: 0; box-sizing: border-box; }
  html, body {
    width: 1000px; height: 1200px; overflow: hidden;
    background: var(--stage);
    font-family: "Source Sans 3", sans-serif;
  }
  .canvas { position: relative; width: 1000px; height: 1200px; }
  .card { position: absolute; left: 76px; width: 826px; overflow: hidden; }

  /* Front */
  .card-front { top: 25px; height: 524px; background: var(--paper); }
  .brand { position: absolute; left: 150px; top: 62px; display: flex; align-items: center; gap: 22px; }
  .brand-dot { width: 58px; height: 58px; border-radius: 50%; background: var(--orange); }
  .brand-name { font-size: 84px; font-weight: 600; color: var(--navy); letter-spacing: 2px; line-height: 1; }
  .person { position: absolute; left: 47px; top: 306px; }
  .person-name { font-size: 31px; font-weight: 600; color: var(--navy); line-height: 1.15; }
  .person-title { font-size: 27px; color: var(--orange); line-height: 1.3; }
  .contact { position: absolute; left: 395px; top: 252px; font-size: 29px; color: var(--navy); line-height: 1; }
  .contact-line { height: 32px; display: flex; align-items: center; white-space: nowrap; }
  .contact-line.gap { height: 36px; }
  .label { color: var(--orange); font-weight: 600; margin-right: 7px; }
  .spacer { display: inline-block; width: 18px; }
  .band { position: absolute; left: 0; bottom: 0; width: 100%; height: 75px; background: var(--navy); }
  .website { position: absolute; right: 47px; top: 50%; transform: translateY(-50%); font-size: 30px; font-weight: 700; color: var(--orange); }

  /* Back */
  .card-back { top: 609px; height: 534px; background: var(--navy); }
  .sun-artwork { position: absolute; left: 0; top: 0; width: 478px; height: 380px;
                 background: linear-gradient(135deg, var(--warm-light) 0%, var(--orange) 100%); }
  .division { position: absolute; left: 311px; top: 386px; color: var(--paper); }
  .division-equation { font-size: 34px; font-weight: 700; line-height: 1.1; white-space: nowrap; }
  .tagline { font-size: 27px; font-style: italic; line-height: 33px; margin-top: 2px; white-space: nowrap; }
</style>
</head>
<body>
<div class="canvas">
  <section class="card card-front">
    <div class="brand">
      <span class="brand-dot"></span>
      <span class="brand-name">TALVEN</span>
    </div>
    <div class="person">
      <div class="person-name">Maren Holt</div>
      <div class="person-title">President</div>
    </div>
    <div class="contact">
      <div class="contact-line">4120 Cedar Ridge Lane</div>
      <div class="contact-line">Fairmont Hills, CA 95800</div>
      <div class="contact-line gap"><span class="label">O:</span>916-555-0142<span class="spacer"></span><span class="label">M:</span>916-555-0187</div>
      <div class="contact-line gap"><span class="label">F:</span>916-555-0163</div>
      <div class="contact-line gap"><span class="label">E:</span>mholt@talven.com</div>
    </div>
    <div class="band">
      <span class="website">www.talven.com</span>
    </div>
  </section>

  <section class="card card-back">
    <div class="sun-artwork" role="img" aria-label="Area for the large sun illustration with rays lighting the blue background"></div>
    <div class="division">
      <div class="division-equation">Talven + Insight = TalvenInsight</div>
      <div class="tagline">Offering Vision, Creativity, and Resilience<br>To Individuals and Organisations</div>
    </div>
  </section>
</div>
</body>
</html>
```